New Company Business Card Design

I have a new company logo and I want a new business card design. I dont know if the logo file i attached is in the correct format or quality. We are a New York City Specialty construction Firm specializing in high risk out of the box projects. I want a simple and classy business card that people will his card is as crisp as the work his company does.

Target Market(s)

Clients in the heavy construction industry in New York City

Industry/Entity Type

Construction Company

Contact Information for Business Card

Simple Classy - DIFFERENT

Font styles to use
Other font styles liked:
• Mach the logo font in some way

Colors

Designer to choose colors to be used in the design.

Requirements
Must have
• Uniqueness
Nice to have
• Nothing particular - Just different and classy - Timeless
Should not have
• Goofy Shit or Gimmicky shit

```html
<!DOCTYPE html>
<html lang="en">
<head>
<meta charset="utf-8">
<title>Korvath Builders – Business Card</title>
<link rel="stylesheet" href="https://fonts.googleapis.com/css2?family=Roboto:wght@400;500;700;900&display=swap">
<style>
  :root {
    --backdrop: #2a2a2a;
    --card-light: #f4f4f3;
    --card-dark: #121212;
    --brand-blue: #1f73c0;
    --brand-blue-deep: #12549a;
    --ink: #2a2a2a;
    --ink-soft: #3a3a3a;
    --paper-white: #ffffff;
    --ghost-light: rgba(150,150,150,0.16);
    --ghost-dark: rgba(255,255,255,0.05);
  }
  * { margin: 0; padding: 0; box-sizing: border-box; }
  html, body {
    width: 1200px; height: 1200px; overflow: hidden;
    background: var(--backdrop);
    font-family: "Roboto", Arial, sans-serif;
  }
  .card {
    position: absolute; left: 250px; width: 760px; height: 434px; overflow: hidden;
  }
  .card--front { top: 149px; background: var(--card-light); }
  .card--back { top: 611px; background: var(--card-dark); }

  .crane-backdrop {
    position: absolute; left: 206px; top: 0; width: 504px; height: 100%;
  }
  .card--front .crane-backdrop {
    background: linear-gradient(135deg, var(--ghost-light), rgba(150,150,150,0.04) 70%);
  }
  .card--back .crane-backdrop {
    background: linear-gradient(135deg, var(--ghost-dark), rgba(255,255,255,0.01) 70%);
  }

  .brand-name {
    position: absolute; text-align: center;
    color: var(--brand-blue); font-weight: 900; text-transform: uppercase;
    line-height: 1;
  }
  .brand-name__main { display: block; letter-spacing: 1px; }
  .brand-name__sub { display: block; letter-spacing: 4px; }
  .card--front .brand-name { left: 470px; top: 62px; width: 254px; }
  .card--front .brand-name__main { font-size: 58px; }
  .card--front .brand-name__sub { font-size: 15px; margin-top: 10px; }
  .card--back .brand-name { left: 190px; top: 150px; width: 380px; }
  .card--back .brand-name__main { font-size: 84px; }
  .card--back .brand-name__sub { font-size: 21px; margin-top: 14px; }

  .person { position: absolute; left: 26px; top: 178px; }
  .person__name { font-size: 32px; font-weight: 700; color: var(--brand-blue); letter-spacing: 0.3px; }
  .person__title { font-size: 18px; color: var(--ink); margin-top: 2px; }

  .address {
    position: absolute; left: 26px; top: 266px;
    font-size: 18px; line-height: 22px; color: var(--ink); font-style: normal;
  }

  .contact-strip {
    position: absolute; left: 27px; top: 330px; width: 31px; height: 104px;
    background: linear-gradient(180deg, var(--brand-blue), var(--brand-blue-deep));
  }
  .contact-list { position: absolute; left: 27px; top: 332px; list-style: none; }
  .contact-list li {
    display: flex; align-items: center; height: 25.5px;
    font-size: 18px; color: var(--ink-soft);
  }
  .contact-list svg { width: 31px; height: 18px; flex: none; margin-right: 9px; }

  .edge-tab {
    position: absolute; top: 179px; width: 28px; height: 84px;
    background: linear-gradient(180deg, var(--brand-blue), var(--brand-blue-deep));
  }
  .edge-tab--left { left: 0; border-right: 2px solid var(--paper-white); }
  .edge-tab--right { right: 0; border-left: 2px solid var(--paper-white); }

  .web-address {
    position: absolute; left: 0; width: 100%; top: 384px; text-align: center;
    font-size: 18px; letter-spacing: 2px; color: #e6e6e6;
  }
  .web-address__domain { color: var(--brand-blue); }
</style>
</head>
<body>

<section class="card card--front">
  <div class="crane-backdrop" role="img" aria-label="Faint tower crane silhouette in the background"></div>

  <div class="brand-name">
    <span class="brand-name__main">Korvath</span>
    <span class="brand-name__sub">Builders, Inc.</span>
  </div>

  <div class="person">
    <h1 class="person__name">Daniel Reyes</h1>
    <p class="person__title">Founder &amp; CEO</p>
  </div>

  <address class="address">
    48 Harbor Lane, Suite B<br>
    Brooklyn, NY 11201
  </address>

  <div class="contact-strip"></div>
  <ul class="contact-list">
    <li>
      <svg viewBox="0 0 31 18" aria-hidden="true"><path fill="#fff" d="M11 3.5c.8-.6 1.6-.4 2 .3l1.2 2.1c.3.6.2 1.2-.3 1.6l-.9.7c.6 1.4 1.6 2.5 3 3.2l.7-.9c.4-.5 1-.6 1.6-.3l2.1 1.2c.7.4.9 1.2.3 2l-.8 1c-.6.7-1.6 1-2.6.6C13.5 13.6 10.5 10.6 9.1 6.9c-.4-1 0-2 .7-2.6z"/></svg>
      555 014 2290
    </li>
    <li>
      <svg viewBox="0 0 31 18" aria-hidden="true"><rect x="8" y="4" width="15" height="10" fill="#fff"/><path d="M8 4l7.5 6L23 4" fill="none" stroke="#1f73c0" stroke-width="1.3"/></svg>
      info@korvathbuild.com
    </li>
    <li>
      <svg viewBox="0 0 31 18" aria-hidden="true"><g fill="none" stroke="#fff" stroke-width="1.3"><circle cx="15.5" cy="9" r="7"/><ellipse cx="15.5" cy="9" rx="3" ry="7"/><path d="M8.5 9h14M9.5 5.5h12M9.5 12.5h12"/></g></svg>
      www.korvathbuild.com
    </li>
  </ul>
</section>

<section class="card card--back">
  <div class="crane-backdrop" role="img" aria-label="Faint tower crane silhouette in the background"></div>
  <div class="edge-tab edge-tab--left"></div>
  <div class="edge-tab edge-tab--right"></div>

  <div class="brand-name">
    <span class="brand-name__main">Korvath</span>
    <span class="brand-name__sub">Builders, Inc.</span>
  </div>

  <p class="web-address">www.<span class="web-address__domain">korvathbuild</span>.com</p>
</section>

</body>
</html>
```